Runlark

I have a web site RUNLARK.com that is in serious need of a re-design. The site is mean't to be a portal for an app that I have called RUNLARK which you can see in the app store or googleplay. Take a look and see what you can do.
Updates

Project Deadline Extended
Reason: Still working with designers. The "look" is not quite there but a lot of progress has been made. MB

Industry/Entity Type

Store

```html
<!DOCTYPE html>
<html lang="en">
<head>
<meta charset="utf-8">
<title>Runlark — Sport statistics app</title>
<link href="https://fonts.googleapis.com/css2?family=Open+Sans:ital,wght@0,400;0,600;0,700;1,600&family=Questrial&display=swap" rel="stylesheet">
<style>
:root{
  --navy:#0b3a78;
  --logo-blue:#1b3f90;
  --cyan:#35c8f5;
  --cyan-soft:#8fe3ff;
  --hero-dark:#03121f;
  --white:#ffffff;
  --ink:#1d1d1d;
  --link:#1b3f90;
  --panel:#e4e4e4;
  --tile-border:#1f6fa8;
  --teal:#3fa7a0;
  --teal-light:#5fbcb3;
  --stat-row:#9fb9c4;
  --stat-row-alt:#b7cdd5;
  --badge-dark:#1b1b1b;
  --badge-blue:#2a7fd4;
  --badge-green:#8dc63f;
  --social-green:#6bbd3b;
}
*{box-sizing:border-box;margin:0;padding:0}
html,body{width:969px;height:1200px;overflow:hidden;background:var(--white)}
body{position:relative;font-family:"Questrial",sans-serif;color:var(--ink)}
.abs{position:absolute}

.top-nav{left:0;top:0;width:969px;height:42px;background:var(--navy);display:flex;justify-content:center;align-items:center;font-family:"Open Sans",sans-serif;font-weight:600;font-size:11px;color:var(--white)}
.top-nav a{color:inherit;text-decoration:none;padding:0 20px;line-height:20px}
.top-nav a+a{border-left:1px solid rgba(255,255,255,.7)}

.hero{left:0;top:42px;width:969px;height:498px;overflow:hidden;
  background:radial-gradient(ellipse 520px 330px at 440px 40px,#bff2ff 0%,#39c6f2 22%,#0d86c4 48%,#07416b 72%,var(--hero-dark) 100%)}
.brand{left:0;width:969px;top:55px;display:flex;justify-content:center;align-items:center;gap:14px}
.brand-dot{width:46px;height:46px;border-radius:50%;background:var(--logo-blue)}
.brand-name{font-size:64px;color:var(--logo-blue);line-height:1}
.tagline{left:0;width:969px;top:134px;text-align:center;font-family:"Open Sans",sans-serif;font-style:italic;font-weight:600;font-size:12.5px;color:var(--logo-blue)}

.hero-title{left:20px;top:170px;width:290px;text-align:center;font-weight:400;font-size:27px;line-height:30px;color:var(--white)}
.hero-sub{left:65px;top:288px;width:200px;text-align:center;font-size:13.5px;line-height:18px;color:var(--white)}
.badge{border-radius:5px}
.badge-apple{left:89px;top:358px;width:39px;height:39px;background:var(--badge-blue);border:2px solid #cfe6ff}
.badge-play{left:147px;top:371px;width:104px;height:34px;background:var(--badge-dark);border:1px solid #666}
.badge-android{left:110px;top:419px;width:104px;height:34px;background:var(--badge-green)}

.hero-photo{left:316px;top:162px;width:333px;height:196px;border:4px solid var(--cyan);border-radius:4px;box-shadow:0 0 14px var(--cyan-soft);
  background:linear-gradient(160deg,#2b3a4a 0%,#55606a 35%,#6b4f8a 65%,#2a2450 100%)}
.hero-copy{left:330px;top:386px;width:306px;text-align:center;font-size:13.5px;line-height:17px;color:var(--white)}
.hero-copy p+p{margin-top:13px}

.phone{left:685px;top:160px;width:252px;height:360px;border-radius:40px 40px 0 0;background:linear-gradient(180deg,#3a3a3a,#0d0d0d 30%);box-shadow:0 0 0 2px #222}
.screen{left:15px;top:88px;width:220px;height:290px;background:var(--teal);overflow:hidden}
.screen-head{height:50px;background:var(--white);display:flex;justify-content:center;align-items:center;gap:7px}
.screen-head .dot{width:14px;height:14px;border-radius:50%;background:var(--logo-blue)}
.screen-head span{font-size:24px;color:var(--logo-blue)}
.player{position:relative;height:78px;background:linear-gradient(180deg,var(--teal-light),var(--teal));color:var(--white);font-family:"Open Sans",sans-serif}
.avatar{position:absolute;left:10px;top:8px;width:60px;height:60px;border-radius:50%;background:radial-gradient(circle at 50% 40%,#c79a5a,#3a2a18);border:2px solid #dfe9e9}
.player .label{position:absolute;left:80px;top:6px;font-size:9px;font-weight:700;letter-spacing:.3px}
.player .name{position:absolute;left:80px;top:18px;font-size:20px;font-family:"Questrial",sans-serif}
.player .team{position:absolute;left:80px;top:44px;font-size:12px}
.stat-row{height:30px;display:flex;font-family:"Open Sans",sans-serif;font-size:15px;color:var(--white);border-top:2px solid #d9e6ea}
.stat-row:nth-child(odd){background:var(--stat-row)}
.stat-row:nth-child(even){background:var(--stat-row-alt)}
.stat-row div{flex:1;padding:4px 8px}
.stat-row div+div{border-left:1px solid #dfe9ec}

.features{left:83px;top:562px;width:800px;font-size:13.5px;line-height:17px}
.features h2{font-family:"Open Sans",sans-serif;font-weight:700;font-size:13px;text-transform:uppercase}
.feature-list{display:flex;gap:18px;list-style:none;margin-bottom:16px}
.feature-list li::before{content:"• "}
.features h3{font-family:"Open Sans",sans-serif;font-weight:700;font-size:13px}

.tiles{left:84px;top:706px;width:820px;height:140px}
.tile{position:absolute;top:0;width:137px;height:131px;border:2px solid var(--tile-border);box-shadow:0 12px 10px -6px rgba(0,0,0,.45)}
.tile-baseball{left:0;background:linear-gradient(180deg,#3e6b32,#6a9a45 55%,#8a6a45)}
.tile-football{left:155px;background:linear-gradient(180deg,#1b2a24,#3f5b48 50%,#5c7a45)}
.tile-soccer{left:319px;background:linear-gradient(180deg,#c9d3c6,#5f9a48 60%,#3f7a30)}
.tile-hockey{left:487px;background:linear-gradient(180deg,#f4f6f8,#dfe4ea 55%,#b3282c)}
.tile-basketball{left:653px;background:linear-gradient(160deg,#1a1410,#6b3a1c 50%,#c8782f)}

.panel{left:46px;top:859px;width:875px;height:297px;background:var(--panel)}
.panel-block{left:83px;width:800px;font-size:13.5px;line-height:17px}
.panel-block h3{font-family:"Open Sans",sans-serif;font-weight:700;font-size:13px;line-height:17px}
.on-the-go{top:870px}
.on-the-go-more{top:924px}
.read-more{left:83px;top:980px;display:flex;align-items:center;gap:6px;height:22px;padding:0 8px;background:var(--navy);color:var(--white);font-family:"Open Sans",sans-serif;font-weight:700;font-size:9px;text-decoration:none}
.read-more .arrow{width:12px;height:12px;border-radius:50%;background:var(--white);position:relative}
.read-more .arrow::after{content:"";position:absolute;left:4px;top:3px;border-left:5px solid var(--navy);border-top:3px solid transparent;border-bottom:3px solid transparent}
.stats-demand{top:1026px}
.quick-links{left:83px;top:1109px;display:grid;grid-template-columns:157px 156px 157px 220px;font-size:13.5px;line-height:17px;white-space:nowrap}
.quick-links .current{color:var(--link);font-weight:700;font-family:"Open Sans",sans-serif;font-size:13px}

.follow{left:789px;top:979px;width:180px;height:59px;background:var(--navy);border-radius:26px 0 0 26px}
.follow-icons{position:absolute;left:20px;top:-14px;display:flex;gap:6px}
.follow-icons span{width:33px;height:33px;border-radius:4px;background:var(--social-green);border:2px solid var(--white)}
.follow-label{position:absolute;left:0;width:150px;top:32px;text-align:center;color:var(--white);font-family:"Open Sans",sans-serif;font-weight:700;font-size:13px}

.footer{left:0;top:1156px;width:969px;height:44px;background:var(--navy);display:flex;justify-content:center;align-items:center;font-family:"Open Sans",sans-serif;font-weight:700;font-size:13px;color:var(--white)}
</style>
</head>
<body>

<nav class="top-nav abs">
  <a href="#">FAQ</a><a href="#">About Us</a><a href="#">Contacts</a>
</nav>

<header class="hero abs">
  <div class="brand abs"><span class="brand-dot"></span><span class="brand-name">Runlark</span></div>
  <div class="tagline abs">The sport statistics and information you want when you want them</div>

  <h1 class="hero-title abs">Watching a sporting event and need information?</h1>
  <p class="hero-sub abs">Select the compatible digital distribution platform for apps to your smart phone...</p>
  <span class="badge badge-apple abs"></span>
  <span class="badge badge-play abs"></span>
  <span class="badge badge-android abs"></span>

  <div class="hero-photo abs" role="img" aria-label="Photo of a basketball game with a player driving to the basket"></div>
  <div class="hero-copy abs">
    <p>RUNLARK has all the up front stats you need whether you are a casual sports fan, a sports junkie or a fantasy league player.</p>
    <p>It is all here and easy to use.</p>
  </div>

  <div class="phone abs">
    <div class="screen abs">
      <div class="screen-head"><span class="dot"></span><span>Runlark</span></div>
      <div class="player">
        <div class="avatar" role="img" aria-label="Player portrait"></div>
        <div class="label">LIVE UPDATE STATISTICS</div>
        <div class="name">Dario Vance</div>
        <div class="team">Harbor City Gulls</div>
      </div>
      <div class="stats">
        <div class="stat-row"><div>MP&nbsp; 42:53</div><div>FG&nbsp;&nbsp; 1</div></div>
        <div class="stat-row"><div>FGA&nbsp;&nbsp; 7</div><div>FG%&nbsp; .143</div></div>
        <div class="stat-row"><div>MP&nbsp; 42:53</div><div>3P&nbsp;&nbsp; 1</div></div>
      </div>
    </div>
  </div>
</header>

<section class="features abs">
  <h2>Runlark provides immediate access to the information you need:</h2>
  <ul class="feature-list">
    <li>Team Statistics</li><li>Player Background</li><li>Live Scores</li><li>Schedules</li><li>Past Team and Player Performance</li>
  </ul>
  <h3>END THE HASSLE!</h3>
  <p>Why bother visiting different websites to find live scores, player stats, schedules and past game performance. All of this is available on RUNLARK.&nbsp; This easy to use app puts it all at your fingertips. Simply select from the convenient drop down menus and tabs and you can research a team, it's match-ups or a player by their name or jersey number.</p>
</section>

<div class="tiles abs">
  <div class="tile tile-baseball" role="img" aria-label="Baseball pitcher throwing on the mound"></div>
  <div class="tile tile-football" role="img" aria-label="Football players at the line of scrimmage"></div>
  <div class="tile tile-soccer" role="img" aria-label="Soccer player's feet at the ball"></div>
  <div class="tile tile-hockey" role="img" aria-label="Ice hockey players on the rink"></div>
  <div class="tile tile-basketball" role="img" aria-label="Basketball player going up with the ball"></div>
</div>

<div class="panel abs"></div>

<section class="panel-block on-the-go abs">
  <h3>On The Go And You Need To Know</h3>
  <p>Not a problem. RUNLARK has the live scores you want on a variety of sports. Download the app and you are on your way.</p>
</section>
<p class="panel-block on-the-go-more abs">So, you're watching a game and want to know how another competition is shaping up or you want to find out the stats of a team or player?&nbsp; Well, RUNLARK has all this information and more. It's easy to naviate and will get you the stats you want without getting distracted from the game. Flick of a finger and the information is yours.</p>
<a class="read-more abs" href="#"><span class="arrow"></span>READ MORE</a>

<section class="panel-block stats-demand abs">
  <h3>Sport Stats on Demand</h3>
  <p>Forget about relying on sportscasters or the banner moving on the bottom of your screen for the scores you want. Just select your league, go to team data, go to the game you're interested in and get the score. All in a matter of seconds.</p>
</section>

<div class="quick-links abs">
  <span class="current">select your league</span><span>select your team</span><span>get team stats</span><span>get player stats</span>
  <span>get the schedule</span><span>get live scores</span><span>get venue information</span><span>find out who refed the game</span>
</div>

<aside class="follow abs">
  <div class="follow-icons"><span></span><span></span><span></span></div>
  <div class="follow-label">Follow us</div>
</aside>

<footer class="footer abs">©2014 by Runlark. Proudly created with Sitecraft.io</footer>

</body>
</html>
```